Need to create a website for a luxury custom home builder in Phoenix USA. Looking forward for some creative designs including a full page video intro on homepage and should show up pretty luxurious.

```html
<!DOCTYPE html>
<html lang="en">
<head>
<meta charset="utf-8">
<title>Keystone Crest Homes — Luxury Custom Homes in Phoenix</title>
<link href="https://fonts.googleapis.com/css2?family=Poppins:wght@300;400;500;600;700&family=Open+Sans:wght@400;600&display=swap" rel="stylesheet">
<style>
:root{
  --accent:#2b9fd8;
  --ink:#1c1f24;
  --muted:#6b7280;
  --soft:#eef5fa;
  --white:#ffffff;
  --footer:#17212a;
  --star:#f5b400;
}
*{box-sizing:border-box;margin:0;padding:0}
html,body{width:1200px;height:4180px;overflow:hidden}
body{font-family:"Open Sans",Arial,sans-serif;color:var(--ink);background:var(--white)}
section{position:relative;width:1200px}

/* Hero */
.hero{height:690px;color:var(--white);overflow:hidden;background:#2a3238}
.hero-photo{position:absolute;inset:0;background:
  linear-gradient(180deg,rgba(20,26,30,.55) 0%,rgba(20,26,30,.15) 30%,rgba(20,26,30,.35) 75%,rgba(15,20,24,.8) 100%),
  linear-gradient(100deg,#7d8a92 0%,#b9c2c6 28%,#e4e2d9 42%,#6f7d6a 62%,#2f4a33 80%,#1d2a22 100%)}
.nav{position:absolute;top:0;left:0;right:0;height:64px;display:flex;align-items:center;padding:0 160px}
.brand{font-family:"Poppins",sans-serif;font-weight:600;font-size:19px;color:var(--white);display:flex;align-items:center;gap:10px}
.brand .dot{width:14px;height:14px;border-radius:50%;background:var(--accent)}
.nav-links{margin-left:auto;display:flex;align-items:center;gap:28px;font-family:"Poppins",sans-serif;font-size:13px}
.nav-links a{color:var(--white);text-decoration:none}
.nav-links a.active{border-bottom:2px solid var(--accent);padding-bottom:4px}
.hero-copy{position:absolute;left:160px;top:250px}
.hero-copy h1{font-family:"Poppins",sans-serif;font-weight:600;font-size:50px;line-height:1.1}
.hero-copy h2{font-family:"Poppins",sans-serif;font-weight:500;font-size:34px;margin-top:6px}
.hero-copy p{font-family:"Poppins",sans-serif;font-weight:300;font-size:23px;letter-spacing:15px;margin-top:8px}
.hero-progress{position:absolute;left:160px;right:560px;top:626px;display:flex;justify-content:space-between;font-size:11px;opacity:.8}
.hero-progress span::after{content:"";display:inline-block;width:50px;height:1px;background:var(--white);margin-left:12px;vertical-align:middle}
.hero-social{position:absolute;right:24px;top:400px;display:flex;flex-direction:column;gap:12px}
.hero-social i{width:10px;height:10px;border-radius:50%;background:rgba(255,255,255,.85);display:block}

/* Intro */
.intro{height:540px;display:flex;align-items:center;padding:0 160px}
.intro-text{width:400px;font-size:19px;line-height:1.62;color:#333}
.intro-text .where{margin-top:60px;font-weight:600;font-size:19px}
.intro-text .where em{font-style:normal;color:var(--accent)}
.intro-visual{margin-left:auto;margin-right:100px;width:300px;height:300px;background:linear-gradient(165deg,#9fd3f0 0%,#e6f0f4 45%,#3ba7d9 70%,#6f9a6a 100%)}

/* Custom built */
.custom{height:530px;background:var(--soft);text-align:center;padding-top:68px}
.section-title{font-family:"Poppins",sans-serif;font-size:36px;font-weight:400;letter-spacing:1px}
.section-title b{font-weight:600}
.custom .lead{width:440px;margin:4px auto 0;font-size:12px;color:var(--muted);line-height:1.5}
.cards{display:flex;gap:24px;justify-content:center;margin-top:22px;position:relative}
.card{width:276px;text-align:center}
.card .photo{height:200px;background:linear-gradient(180deg,#8fc6ea 0%,#dfeaf1 35%,#f4f4f2 55%,#5a92b4 80%,#2f6d8e 100%)}
.card.night .photo{background:linear-gradient(180deg,#0f1c2e 0%,#243a55 40%,#d7e2e8 62%,#2aa0d6 85%,#13547a 100%)}
.card.featured .photo{background:linear-gradient(160deg,#2b9fd8,#1f7fb3);display:flex;align-items:center;justify-content:center}
.card h3{font-family:"Poppins",sans-serif;font-size:14px;font-weight:500;margin-top:14px}
.card p{font-size:11px;color:var(--muted);margin-top:4px}
.arrow{position:absolute;top:86px;width:28px;height:28px;border-radius:50%;background:var(--white);display:flex;align-items:center;justify-content:center;box-shadow:0 1px 4px rgba(0,0,0,.12)}

/* Projects */
.projects{height:730px;text-align:center;padding-top:70px}
.grid{position:relative;width:880px;height:470px;margin:40px auto 0}
.grid div{position:absolute}
.p1{left:0;top:0;width:285px;height:470px;background:linear-gradient(180deg,#9cc4e4 0%,#cfe0ec 25%,#f1f1ee 45%,#b6b2a6 62%,#5f8a45 80%,#3e6a2e 100%)}
.p2{left:300px;top:0;width:340px;height:220px;background:linear-gradient(180deg,#d3e1ea 0%,#f2efe6 40%,#d8cfbd 70%,#8c8470 100%)}
.p3{left:655px;top:0;width:225px;height:220px;background:linear-gradient(180deg,#b9d2e6 0%,#dcdcd8 45%,#8c8f86 70%,#5a7a48 100%)}
.p4{left:300px;top:235px;width:225px;height:235px;background:linear-gradient(180deg,#a9c7e2 0%,#c9ccc9 40%,#6d706c 65%,#4e6d3e 100%)}
.p5{left:540px;top:235px;width:340px;height:235px;background:linear-gradient(180deg,#1a2c48 0%,#3c5677 35%,#c9cfd3 60%,#e8c88e 80%,#5a5a52 100%)}
.btn{display:inline-block;margin-top:26px;border:1px solid var(--accent);color:var(--accent);font-size:12px;padding:8px 22px}

/* Testimonials */
.testimonials{height:640px;background:var(--soft);text-align:center;padding-top:76px}
.quotes{display:flex;gap:28px;justify-content:center;margin-top:36px}
.quote{width:256px;height:390px;background:var(--white);box-shadow:0 2px 10px rgba(0,0,0,.06);padding:36px 22px 0}
.avatar{width:62px;height:62px;border-radius:50%;margin:0 auto;background:linear-gradient(160deg,#d8c7b4,#6f5e52)}
.avatar.dark{background:linear-gradient(160deg,#3a3a3a,#111)}
.stars{color:var(--star);font-size:14px;letter-spacing:2px;margin-top:16px}
.quote p{font-size:12.5px;line-height:1.65;color:var(--muted);margin-top:12px}
.quote .who{font-size:12px;color:var(--ink);margin-top:12px}
.dots{margin-top:30px;display:flex;justify-content:center;gap:8px}
.dots i{width:7px;height:7px;border-radius:50%;background:#bcd6e6;display:block}
.dots i.on{background:var(--accent)}

/* News */
.news{height:640px;padding-top:70px;text-align:center}
.news-grid{position:relative;width:880px;height:420px;margin:40px auto 0;text-align:left}
.post{position:absolute;color:var(--white);overflow:hidden}
.post .shade{position:absolute;inset:0}
.post .meta{position:absolute;left:20px;bottom:18px;right:20px}
.post .date{font-size:11px;display:flex;align-items:center;gap:6px}
.post .date::before{content:"";width:10px;height:10px;background:#2fbf71;display:inline-block}
.post h3{font-family:"Poppins",sans-serif;font-size:15px;font-weight:500;margin-top:6px;line-height:1.35}
.n1{left:0;top:0;width:430px;height:420px}
.n1 .shade{background:linear-gradient(180deg,#a9c3d8 0%,#e4e4de 30%,#9a8a78 55%,#4e5a3e 75%,#15191d 100%)}
.n2{left:448px;top:0;width:432px;height:200px}
.n2 .shade{background:linear-gradient(180deg,#1b2733 0%,#3b4a44 35%,#c9a160 55%,#2b3530 75%,#0f1418 100%)}
.n3{left:448px;top:220px;width:432px;height:200px}
.n3 .shade{background:linear-gradient(180deg,#e39a5c 0%,#9c7a78 30%,#3d3f4a 55%,#2e7fa8 72%,#101318 100%)}

/* Footer */
.footer{height:360px;margin-top:40px;background:linear-gradient(180deg,rgba(23,33,42,.85),var(--footer)),linear-gradient(90deg,#3a4650,#24303a);color:var(--white);text-align:center;padding-top:56px}
.footer .brand{justify-content:center;font-size:21px}
.footer-nav{display:flex;justify-content:center;gap:30px;font-family:"Poppins",sans-serif;font-size:12px;margin-top:22px}
.contact{display:flex;justify-content:space-between;width:880px;margin:40px auto 0;text-align:left;font-size:12px}
.contact div{display:flex;align-items:center;gap:12px}
.contact .ic{width:44px;height:44px;border-radius:50%;background:var(--accent);display:flex;align-items:center;justify-content:center;flex:none}
.copy{font-size:11px;opacity:.7;margin-top:28px}
.socials{display:flex;justify-content:center;gap:10px;margin-top:12px}
.socials i{width:22px;height:22px;border-radius:50%;background:rgba(255,255,255,.2);display:block}
.socials i.on{background:var(--accent)}
</style>
</head>
<body>

<section class="hero">
  <div class="hero-photo" role="img" aria-label="Full-width video of a modern luxury home with pool and palm trees"></div>
  <nav class="nav">
    <div class="brand"><span class="dot"></span>Keystone Crest Homes</div>
    <div class="nav-links">
      <a class="active">Home</a><a>About Us</a><a>Services</a><a>Gallery</a><a>Reviews</a><a>Contact Us</a>
      <svg width="14" height="14" viewBox="0 0 14 14"><circle cx="6" cy="6" r="4.5" fill="none" stroke="#fff" stroke-width="1.6"/><line x1="9.5" y1="9.5" x2="13" y2="13" stroke="#fff" stroke-width="1.6"/></svg>
    </div>
  </nav>
  <div class="hero-copy">
    <h1>Explore visions</h1>
    <h2>without boundries, we build</h2>
    <p>the Future imagined</p>
  </div>
  <div class="hero-social"><i></i><i></i><i></i><i></i></div>
  <div class="hero-progress"><span>01 Intro</span><span>Scroll Down</span></div>
</section>

<section class="intro">
  <div class="intro-text">
    <p>Lorem ipsum dolor sit amet, consectetur adipiscing elit. Mauris fringilla odio sed sem dictum, vitae volutpat mauris rhoncus. Vivamus tincidunt aliquam ex at interdum ut. Quisque at erat in orci hendrerit fringilla at a nisl.</p>
    <p class="where">We Work in <em>Phoenix USA.</em></p>
  </div>
  <div class="intro-visual" role="img" aria-label="Photo of a white Phoenix home with pool under blue sky"></div>
</section>

<section class="custom">
  <h2 class="section-title"><b>CUSTOM BUILT</b> HOMES</h2>
  <p class="lead">Lorem ipsum is simply dummy text of the printing and typesetting industry. Lorem ipsum has been the industry's standard dummy text.</p>
  <div class="cards">
    <span class="arrow" style="left:90px"><svg width="10" height="10" viewBox="0 0 10 10"><path d="M6.5 1.5 3 5l3.5 3.5" fill="none" stroke="#888" stroke-width="1.4"/></svg></span>
    <div class="card"><div class="photo" role="img" aria-label="White modern custom home with pool"></div><h3>Custom Home Title</h3><p>It is a long established fact that...</p></div>
    <div class="card featured"><div class="photo" role="img" aria-label="Custom home highlighted in blue"><svg width="30" height="30" viewBox="0 0 30 30"><circle cx="15" cy="15" r="13" fill="none" stroke="#fff" stroke-width="1.5"/><path d="M13 10l5 5-5 5" fill="none" stroke="#fff" stroke-width="1.5"/></svg></div><h3>Custom Home Title</h3><p>It is a long established fact that...</p></div>
    <div class="card night"><div class="photo" role="img" aria-label="Modern villa lit at night beside pool"></div><h3>Custom Home Title</h3><p>It is a long established fact that...</p></div>
    <span class="arrow" style="right:90px"><svg width="10" height="10" viewBox="0 0 10 10"><path d="M3.5 1.5 7 5 3.5 8.5" fill="none" stroke="#888" stroke-width="1.4"/></svg></span>
  </div>
</section>

<section class="projects">
  <h2 class="section-title">OUR <b>PROJECTS</b></h2>
  <div class="grid">
    <div class="p1" role="img" aria-label="Two-storey family house with lawn"></div>
    <div class="p2" role="img" aria-label="White contemporary house with balconies"></div>
    <div class="p3" role="img" aria-label="Modern two-storey home exterior"></div>
    <div class="p4" role="img" aria-label="Grey modern house with garden"></div>
    <div class="p5" role="img" aria-label="Contemporary home lit at twilight"></div>
  </div>
  <a class="btn">View Full Portfolio</a>
</section>

<section class="testimonials">
  <h2 class="section-title">WHAT PEOPLE <b>ARE SAYING</b></h2>
  <div class="quotes">
    <div class="quote"><div class="avatar" role="img" aria-label="Client portrait"></div><div class="stars">★★★★★</div><p>Our new home was finished on time and the team kept us informed at every step. The quality of the work is excellent and we love living here every day.</p><p class="who">– Dana Smith</p></div>
    <div class="quote"><div class="avatar dark" role="img" aria-label="Client portrait"></div><div class="stars">★★★★★</div><p>Our new home was finished on time and the team kept us informed at every step. The quality of the work is excellent and we love living here every day.</p><p class="who">– Alex Rowe</p></div>
    <div class="quote"><div class="avatar" role="img" aria-label="Client portrait"></div><div class="stars">★★★★★</div><p>Our new home was finished on time and the team kept us informed at every step. The quality of the work is excellent and we love living here every day.</p><p class="who">– Bryn Dale</p></div>
  </div>
  <div class="dots"><i></i><i class="on"></i><i></i><i></i></div>
</section>

<section class="news">
  <h2 class="section-title">LATEST <b>NEWS</b></h2>
  <div class="news-grid">
    <article class="post n1"><div class="shade" role="img" aria-label="Large brick family house with front lawn"></div><div class="meta"><p class="date">15 Oct 2022</p><h3>Lorem Ipsum is simply dummy text of the printing and typesetting industry</h3></div></article>
    <article class="post n2"><div class="shade" role="img" aria-label="Modern home with lit windows at night"></div><div class="meta"><p class="date">12 Oct 2022</p><h3>It is a long established fact that a reader</h3></div></article>
    <article class="post n3"><div class="shade" role="img" aria-label="Modern house with pool at sunset"></div><div class="meta"><p class="date">08 Oct 2022</p><h3>Contrary to popular belief, Lorem Ipsum is not simply</h3></div></article>
  </div>
</section>

<footer class="footer">
  <div class="brand"><span class="dot"></span>Keystone Crest Homes</div>
  <div class="footer-nav"><span>Home</span><span>About</span><span>Our Projects</span><span>Latest News</span><span>Contact Us</span></div>
  <div class="contact">
    <div><span class="ic"><svg width="18" height="18" viewBox="0 0 18 18"><path d="M9 1.5a5.5 5.5 0 0 0-5.5 5.5C3.5 11 9 16.5 9 16.5S14.5 11 14.5 7A5.5 5.5 0 0 0 9 1.5z" fill="#fff"/><circle cx="9" cy="7" r="2" fill="#2b9fd8"/></svg></span><span>120, Lorem Street, Suite 4,<br>Phoenix, AZ, USA</span></div>
    <div><span class="ic"><svg width="18" height="18" viewBox="0 0 18 18"><rect x="2" y="4" width="14" height="10" rx="1" fill="#fff"/><path d="M2.5 4.5 9 10l6.5-5.5" fill="none" stroke="#2b9fd8" stroke-width="1.3"/></svg></span><span>info@keystonecrest.com</span></div>
    <div><span class="ic"><svg width="18" height="18" viewBox="0 0 18 18"><path d="M5 2l2.5 3-1.5 2a9 9 0 0 0 5 5l2-1.5 3 2.5-1.5 2.5C8 15.5 2.5 10 2.5 3.5z" fill="#fff"/></svg></span><span style="font-size:16px">(480) 555-0142</span></div>
  </div>
  <p class="copy">© 2022 Keystone Crest Homes. All Rights Reserved.</p>
  <div class="socials"><i></i><i class="on"></i><i></i></div>
</footer>

</body>
</html>
```